Sales Brochure

We are looking for an 8.5 x 11 folding brochure in a landscape orientation that advertises our product and service offerings. This brochure should have content on both sides.

This brochure would be left at prospect client's business, so it needs to be fresh, professional, and focused.

We have attached two 1-page inserts that we would like you to use for inspiration for the written content in the brochure. We would like the main theme of the brochure to focus on professional, repeatable, and quality IT support for business.

The brochure should have the prospective clients email or call (will provide number and email to winner) to get additional information.

Please be creative with both the content and the design.

Went on vacation/holiday

```html
<!DOCTYPE html>
<html lang="en">
<head>
<meta charset="utf-8">
<title>Nordaxis IT Support Brochure</title>
<link href="https://fonts.googleapis.com/css2?family=Montserrat:wght@500;600;700&family=Arimo:wght@400;700&display=swap" rel="stylesheet">
<style>
:root{
  --stage:#676767;
  --paper:#dedede;
  --paper-shade:#a8a8a8;
  --brand:#1592d0;
  --ink:#1c1c1c;
  --muted:#4d4d4d;
  --bar:#000000;
  --white:#ffffff;
  --watermark:#d2d2d2;
}
*{margin:0;padding:0;box-sizing:border-box}
html,body{width:1200px;height:3000px;overflow:hidden;background:var(--stage)}
body{position:relative;font-family:"Arimo",Arial,sans-serif;color:var(--ink)}
.panel{position:absolute;left:138px;width:925px;background:var(--paper);overflow:hidden}
.panel-front{top:145px;height:1197px}
.panel-inside{top:1675px;height:1197px}

/* front */
.hero{position:absolute;left:0;top:0;width:925px;height:491px;
  background:linear-gradient(100deg,#e9e6e2 0%,#d6cfc7 22%,#b9814f 36%,#efe7dc 55%,#6c6258 72%,#3b3a3c 88%,#2a2a2d 100%)}
.hero-rule{position:absolute;left:0;top:491px;width:925px;height:5px;background:var(--brand)}
.wordmark{position:absolute;left:58px;top:50px;font-family:"Montserrat",Arial,sans-serif;font-weight:700;
  font-size:50px;letter-spacing:3px;color:var(--brand)}
.hero-url{position:absolute;right:40px;top:462px;font-size:17px;letter-spacing:4px;color:var(--white)}
.service-bar{position:absolute;left:0;top:504px;width:925px;height:95px;background:var(--bar);
  display:flex;justify-content:space-around}
.service{width:231px;text-align:center;padding-top:14px;color:var(--white);font-weight:700;font-size:12px;letter-spacing:1.5px}
.service svg{display:block;margin:0 auto 8px;width:50px;height:42px}
.front-field{position:absolute;left:0;top:599px;width:925px;height:598px;
  background:linear-gradient(var(--paper-shade) 0,var(--paper) 90px)}
.watermark-name{position:absolute;left:0;width:925px;top:225px;text-align:center;font-family:"Montserrat",Arial,sans-serif;
  font-weight:700;font-size:70px;letter-spacing:8px;color:var(--watermark)}
.contact-row{position:absolute;left:56px;right:56px;display:flex;justify-content:space-between;
  font-weight:700;font-size:16px;letter-spacing:2px;color:var(--muted)}
.contact-row span,.strip .contact{display:inline-flex;align-items:center;gap:4px}
.contact-row svg,.strip svg{width:14px;height:14px}
.front-field .contact-row{top:556px}

/* inside */
.lead{position:absolute;left:79px;top:92px;font-weight:700;font-size:20px;letter-spacing:3.3px;color:var(--brand);white-space:nowrap}
.offer{position:absolute;left:34px;width:846px}
.offer-icon{position:absolute;left:42px;top:-6px;width:34px;height:34px;border-radius:50%;background:#ececec;
  box-shadow:-10px 12px 14px rgba(0,0,0,.12);display:flex;align-items:center;justify-content:center}
.offer-icon svg{width:20px;height:20px}
.offer h3{margin-left:93px;font-weight:700;font-size:14px;letter-spacing:2.5px;color:var(--brand)}
.offer p{margin:8px 0 0 93px;font-size:8.4px;line-height:1.3;color:var(--ink);max-width:720px}
.pledge{position:absolute;left:59px;width:815px;top:455px;font-weight:700;font-size:12px;line-height:1.25;
  letter-spacing:2px;color:var(--brand)}
.strip{position:absolute;left:0;top:514px;width:925px;height:85px;background:var(--bar);color:var(--white);
  font-weight:700;font-size:15px;letter-spacing:2px}
.strip .phone{position:absolute;left:88px;top:34px}
.strip .site{position:absolute;right:84px;top:34px}
.strip .brand-name{position:absolute;left:362px;width:200px;top:30px;text-align:center;
  font-family:"Montserrat",Arial,sans-serif;font-weight:700;font-size:20px;letter-spacing:3px;color:var(--brand)}
.plans{position:absolute;left:0;top:599px;width:925px;height:598px;
  background:linear-gradient(var(--paper-shade) 0,var(--paper) 90px)}
.plans-title{position:absolute;left:79px;top:117px;font-weight:700;font-size:23px;line-height:1.16;letter-spacing:3.5px;color:var(--brand)}
.plans-title sup{font-size:14px}
.plans-intro{position:absolute;left:79px;width:767px;top:183px;font-size:8.4px;line-height:1.3}
.plans .contact-row{top:556px}
</style>
</head>
<body>

<section class="panel panel-front">
  <div class="hero" role="img" aria-label="Photo of a man in glasses working at a laptop beside a sunlit window"></div>
  <div class="wordmark">NORDAXIS</div>
  <div class="hero-url">www.nordaxis.com</div>
  <div class="hero-rule"></div>

  <nav class="service-bar">
    <div class="service">
      <svg viewBox="0 0 50 42" fill="none" stroke="#1592d0" stroke-width="3" stroke-linejoin="round"><path d="M5 36V8h13l4 5h18v7"/><path d="M5 36l8-16h33l-8 16z"/></svg>
      Infrastructure
    </div>
    <div class="service">
      <svg viewBox="0 0 50 42"><path d="M13 32a8 8 0 0 1 0-16 11 11 0 0 1 21-3 9 9 0 0 1 4 19z" fill="#1592d0"/><path d="M25 28V17m-5 5l5-5 5 5" stroke="#000" stroke-width="3" fill="none"/></svg>
      Cloud Integration
    </div>
    <div class="service">
      <svg viewBox="0 0 50 42" fill="none" stroke="#1592d0" stroke-width="3"><path d="M12 4h26l6 22v12H6V26z"/><path d="M6 26h38"/><circle cx="34" cy="32" r="1.5" fill="#1592d0"/><circle cx="39" cy="32" r="1.5" fill="#1592d0"/></svg>
      Desktop Support
    </div>
    <div class="service">
      <svg viewBox="0 0 50 42" fill="#1592d0"><rect x="8" y="34" width="4" height="4"/><rect x="15" y="30" width="5" height="8"/><rect x="23" y="24" width="5" height="14"/><rect x="31" y="16" width="5" height="22"/><rect x="39" y="6" width="5" height="32"/></svg>
      Data Protection
    </div>
  </nav>

  <div class="front-field">
    <div class="watermark-name">NORDAXIS</div>
    <div class="contact-row">
      <span><svg viewBox="0 0 14 14"><circle cx="7" cy="7" r="6.5" fill="#4d4d4d"/><path d="M1 7h12M7 1c-3 3-3 9 0 12M7 1c3 3 3 9 0 12" stroke="#dedede" fill="none"/></svg>www.nordaxis.com</span>
      <span><svg viewBox="0 0 14 14"><circle cx="7" cy="7" r="6.5" fill="#4d4d4d"/><path d="M4.5 3.5l2 2-1 1c.5 1 1.5 2 2.5 2.5l1-1 2 2-1.3 1.3C6.5 11 3 7.5 3.2 4.8z" fill="#dedede"/></svg>555-014-2290</span>
      <span><svg viewBox="0 0 14 14"><circle cx="7" cy="7" r="6.5" fill="#4d4d4d"/><path d="M7 11.5S4 8 4 6a3 3 0 0 1 6 0c0 2-3 5.5-3 5.5z" fill="#dedede"/></svg>88 Ridge Avenue Box 402, Elm Falls, AB</span>
    </div>
  </div>
</section>

<section class="panel panel-inside">
  <h2 class="lead">Here are a few ways in which we take care of your IT needs:</h2>

  <div class="offer" style="top:151px">
    <div class="offer-icon"><svg viewBox="0 0 20 20" fill="none" stroke="#1592d0" stroke-width="1.6"><path d="M5 3h10l3 10v4H2v-4z"/><path d="M2 13h16"/></svg></div>
    <h3>DESKTOP SUPPORT</h3>
    <p>Our support technicians answer calls and tickets logged in our online help desk around the clock. Most issues are solved quickly through remote sessions, and when a visit is needed a technician comes on-site. Regular check-ins and short surveys make sure you stay happy with the help you receive.</p>
  </div>
  <div class="offer" style="top:237px">
    <div class="offer-icon"><svg viewBox="0 0 20 20" fill="none" stroke="#1592d0" stroke-width="1.6"><circle cx="10" cy="10" r="7"/><circle cx="10" cy="10" r="2"/><path d="M10 3v5M10 12v5M3 10h5M12 10h5"/></svg></div>
    <h3>SYSTEMS MANAGEMENT</h3>
    <p>We put our know-how in systems and networks (mail, servers, cloud, wireless, printing and remote access) to work for you.</p>
  </div>
  <div class="offer" style="top:305px">
    <div class="offer-icon"><svg viewBox="0 0 20 20" fill="#1592d0"><rect x="3" y="15" width="2" height="2"/><rect x="6" y="13" width="2" height="4"/><rect x="9" y="10" width="2" height="7"/><rect x="12" y="7" width="2" height="10"/><rect x="15" y="3" width="2" height="14"/></svg></div>
    <h3>DATA PROTECTION</h3>
    <p>We offer cost effective ways to keep your files backed up safely. We check that every backup runs properly and steadily, and we watch over them each day.</p>
  </div>
  <div class="offer" style="top:385px">
    <div class="offer-icon"><svg viewBox="0 0 20 20" fill="none" stroke="#1592d0" stroke-width="1.4"><rect x="2" y="3" width="16" height="13"/><path d="M5 13l3-4 3 2 4-5"/></svg></div>
    <h3>IT PROJECTS</h3>
    <p>We plan, manage and carry out all your technology projects, meeting the goals we agree on, on time and on budget.</p>
  </div>

  <p class="pledge">We pride ourselves in delivering services that increase your productivity, helping your business run more efficiently and effectively. We are your IT department.</p>

  <div class="strip">
    <span class="contact phone"><svg viewBox="0 0 14 14"><circle cx="7" cy="7" r="6.5" fill="#fff"/><path d="M4.5 3.5l2 2-1 1c.5 1 1.5 2 2.5 2.5l1-1 2 2-1.3 1.3C6.5 11 3 7.5 3.2 4.8z" fill="#000"/></svg>555-014-2290</span>
    <div class="brand-name">NORDAXIS</div>
    <span class="contact site"><svg viewBox="0 0 14 14"><circle cx="7" cy="7" r="6.5" fill="#fff"/><path d="M1 7h12M7 1c-3 3-3 9 0 12M7 1c3 3 3 9 0 12" stroke="#000" fill="none"/></svg>www.nordaxis.com</span>
  </div>

  <div class="plans">
    <h2 class="plans-title">STEADYCARE<sup>TM</sup><br>SERVICE PLANS</h2>
    <p class="plans-intro">Keeping your technology safe and current is not a one-time task. Our SteadyCARE service plans bring peace of mind for all your technology and infrastructure at a fair price. Knowing your computers are safe and well kept saves you stress, so you can focus on what you do best. Our plans secure your workstations, tune your servers and network, and keep your data safe.</p>

    <div class="offer" style="top:257px">
      <div class="offer-icon"><svg viewBox="0 0 20 20" fill="none" stroke="#1592d0" stroke-width="1.4"><rect x="8" y="3" width="10" height="8"/><circle cx="5" cy="5" r="2"/><path d="M3 17V9h4l2 4h6v4"/></svg></div>
      <h3>STEADYCARE™ WORKSTATION</h3>
      <p>We provide quick, quality IT help to Elm Falls and the nearby towns. Our SteadyCARE plans give fast response times, and our project services bring skilled IT help at a fair price. Professional, reliable service is our standard.</p>
    </div>
    <div class="offer" style="top:338px">
      <div class="offer-icon"><svg viewBox="0 0 20 20" fill="none" stroke="#1592d0" stroke-width="1.5" stroke-linejoin="round"><path d="M2 16V4h5l2 2h7v3"/><path d="M2 16l3-7h13l-3 7z"/></svg></div>
      <h3>STEADYCARE™ INFRASTRUCTURE</h3>
      <p>Our SteadyCARE Infrastructure plan keeps your servers and other key network devices running at their best. This includes routine care tasks, monitoring and alerts. Because we know your IT setup, we can act fast on any issue that comes up, which greatly shortens recovery times.</p>
    </div>
    <div class="offer" style="top:428px">
      <div class="offer-icon"><svg viewBox="0 0 20 20" fill="#1592d0"><rect x="3" y="15" width="2" height="2"/><rect x="6" y="13" width="2" height="4"/><rect x="9" y="10" width="2" height="7"/><rect x="12" y="7" width="2" height="10"/><rect x="15" y="3" width="2" height="14"/></svg></div>
      <h3>STEADYCARE™ DATA PROTECTION</h3>
      <p>When did you last run a full backup of your data and then test it to be sure it restores properly? SteadyCARE Data Protection means we check your backups every day. Failed jobs are flagged to our team, we find the cause and make changes so the next backup runs well. This way a clean, current copy of your data is always kept. We also check file integrity to confirm the backups are valid, and run test restores from time to time.</p>
    </div>

    <div class="contact-row">
      <span><svg viewBox="0 0 14 14"><circle cx="7" cy="7" r="6.5" fill="#4d4d4d"/><path d="M1 7h12M7 1c-3 3-3 9 0 12M7 1c3 3 3 9 0 12" stroke="#dedede" fill="none"/></svg>www.nordaxis.com</span>
      <span><svg viewBox="0 0 14 14"><circle cx="7" cy="7" r="6.5" fill="#4d4d4d"/><path d="M4.5 3.5l2 2-1 1c.5 1 1.5 2 2.5 2.5l1-1 2 2-1.3 1.3C6.5 11 3 7.5 3.2 4.8z" fill="#dedede"/></svg>555-014-2290</span>
      <span><svg viewBox="0 0 14 14"><circle cx="7" cy="7" r="6.5" fill="#4d4d4d"/><path d="M7 11.5S4 8 4 6a3 3 0 0 1 6 0c0 2-3 5.5-3 5.5z" fill="#dedede"/></svg>88 Ridge Avenue Box 402, Elm Falls, AB</span>
    </div>
  </div>
</section>

</body>
</html>
```